Business Card Design for Property Development Company Director

I am looking for a professional and unforgettable business card design for our Director of our Property Development Company.
Please see attached .pptx file to find out what information to include. You don't have to follow the exact format shown in the file - I am interested to see your creative flair using the information provided.

```html
<!DOCTYPE html>
<html lang="en">
<head>
<meta charset="UTF-8">
<title>Halvern Property Group – Business Card</title>
<link href="https://fonts.googleapis.com/css2?family=Roboto:wght@400;500;700&family=Roboto+Condensed:wght@700&display=swap" rel="stylesheet">
<style>
  :root {
    --backdrop: #e6e7e9;
    --card: #f8f8f8;
    --brand-blue: #2b4c9b;
    --brand-grey: #585a5e;
    --text-grey: #5f6165;
    --shadow: rgba(0, 0, 0, 0.14);
  }
  * { box-sizing: border-box; margin: 0; padding: 0; }
  html, body {
    width: 1200px; height: 726px; overflow: hidden;
    background: var(--backdrop);
    font-family: "Roboto", Arial, sans-serif;
  }
  .stage { position: relative; width: 1200px; height: 726px; }
  .card {
    position: absolute; top: 208px;
    width: 540px; height: 310px;
    background: var(--card);
    box-shadow: 0 6px 18px var(--shadow);
    overflow: hidden;
  }
  .card--front { left: 40px; }
  .card--back { left: 620px; }

  /* Front */
  .front__tagline {
    position: absolute; top: 34px; left: 0; width: 100%;
    text-align: center; color: var(--brand-blue);
    font-size: 19px; line-height: 23px; font-weight: 400;
  }
  .wordmark { position: absolute; display: flex; align-items: center; gap: 14px; }
  .wordmark__square { width: 44px; height: 44px; background: var(--brand-blue); }
  .wordmark__name {
    color: var(--brand-blue); font-weight: 700;
    text-transform: uppercase; line-height: 1;
  }
  .wordmark__name span { display: block; }
  .front__wordmark { top: 110px; left: 112px; }
  .front__wordmark .wordmark__name { font-size: 44px; }
  .front__wordmark .wordmark__name span + span { font-size: 18px; letter-spacing: 6.2px; margin-top: 4px; }
  .front__pitch {
    position: absolute; top: 232px; left: 0; width: 100%;
    text-align: center; color: var(--text-grey); font-size: 15px;
  }
  .front__pitch strong { color: var(--brand-blue); font-weight: 400; }
  .front__band {
    position: absolute; left: 0; bottom: 24px; width: 100%; height: 11px;
    display: flex;
  }
  .front__band-grey { flex: 0 0 52%; background: var(--brand-grey); }
  .front__band-blue { flex: 1; background: var(--brand-blue); }

  /* Back */
  .back__wordmark { top: 36px; left: 34px; }
  .back__wordmark .wordmark__square { width: 36px; height: 36px; }
  .back__wordmark .wordmark__name { font-size: 36px; }
  .back__wordmark .wordmark__name span + span { font-size: 15px; letter-spacing: 4.9px; margin-top: 3px; }
  .contact {
    position: absolute; top: 112px; left: 300px;
    list-style: none; color: var(--text-grey); font-size: 14px;
  }
  .contact li { display: flex; align-items: center; gap: 9px; height: 21px; }
  .contact svg { width: 13px; height: 13px; fill: var(--brand-grey); flex: none; }
  .person { position: absolute; left: 40px; top: 216px; }
  .person__name {
    font-family: "Roboto Condensed", "Arial Narrow", sans-serif;
    font-weight: 700; font-size: 21px; color: var(--brand-blue);
  }
  .person__role { font-size: 14px; color: var(--text-grey); margin-top: 3px; }
  .back__band {
    position: absolute; left: 0; bottom: 0; width: 100%; height: 14px;
    background: var(--brand-grey);
  }
  .licence {
    position: absolute; right: 0; bottom: 14px;
    width: 270px; height: 40px;
    background: var(--brand-blue); color: #fff;
    border-top-left-radius: 16px;
    display: flex; align-items: center; justify-content: center;
    font-size: 14px; letter-spacing: 0.2px;
  }
</style>
</head>
<body>
<main class="stage">
  <section class="card card--front" aria-label="Card front">
    <p class="front__tagline">Property Development<br>&amp; Site Acquisition Specialists</p>
    <div class="wordmark front__wordmark">
      <div class="wordmark__square"></div>
      <div class="wordmark__name"><span>Halvern</span><span>Property Group</span></div>
    </div>
    <p class="front__pitch">Ask me about our <strong>INVESTMENT &amp; PARTNERSHIP</strong> opportunities</p>
    <div class="front__band"><div class="front__band-grey"></div><div class="front__band-blue"></div></div>
  </section>

  <section class="card card--back" aria-label="Card back">
    <div class="wordmark back__wordmark">
      <div class="wordmark__square"></div>
      <div class="wordmark__name"><span>Halvern</span><span>Property Group</span></div>
    </div>
    <ul class="contact">
      <li>
        <svg viewBox="0 0 24 24" aria-hidden="true"><path d="M6.6 10.8a15.1 15.1 0 0 0 6.6 6.6l2.2-2.2a1 1 0 0 1 1-.25 11.4 11.4 0 0 0 3.6.57 1 1 0 0 1 1 1V20a1 1 0 0 1-1 1A17 17 0 0 1 3 4a1 1 0 0 1 1-1h3.5a1 1 0 0 1 1 1c0 1.25.2 2.45.57 3.57a1 1 0 0 1-.25 1z"/></svg>
        0400 218 637
      </li>
      <li>
        <svg viewBox="0 0 24 24" aria-hidden="true"><path d="M2 5h20v14H2zm2 2v.5l8 5 8-5V7zm0 2.8V17h16V9.8l-8 5z"/></svg>
        daniel@halvern.com.au
      </li>
      <li>
        <svg viewBox="0 0 24 24" aria-hidden="true"><path d="M12 2a10 10 0 1 0 0 20 10 10 0 0 0 0-20zm6.9 9h-3a15 15 0 0 0-1.4-6A8 8 0 0 1 18.9 11zM12 4c.9 1.2 1.7 3.7 1.9 7h-3.8C10.3 7.7 11.1 5.2 12 4zM9.5 5a15 15 0 0 0-1.4 6h-3A8 8 0 0 1 9.5 5zm-4.4 8h3a15 15 0 0 0 1.4 6 8 8 0 0 1-4.4-6zm5 0h3.8c-.2 3.3-1 5.8-1.9 7-.9-1.2-1.7-3.7-1.9-7zm4.4 6a15 15 0 0 0 1.4-6h3a8 8 0 0 1-4.4 6z"/></svg>
        www.halvern.com.au
      </li>
    </ul>
    <div class="person">
      <p class="person__name">Daniel Marsh</p>
      <p class="person__role">Director</p>
    </div>
    <div class="licence">Real Estate Lic: 5129384 &amp; 5129385</div>
    <div class="back__band"></div>
  </section>
</main>
</body>
</html>
```